Harbor Compass - Book Cover

I need a book cover for my debut work, "Harbor Compass - Turning the Tide, One Step at a Time." While the website isn't complete, you can get a sense of what I am writing about by looking at my website, harborcompassbooks.org. The book is a leadership development book, but more of a personal change journey. The emphasis is on figuring out how to combine you work, social, and own self into an authentic package that not only resonates with others, but makes what you achieve more fulfilling.

I am attaching a copy of my logo so you can get a sense of what I like. I would prefer to not have the cover be photographic, but am open to suggestions. This will be a series of books so maintaining some sense of style will be important, and can garner future work.

Industry/Entity Type

Leadership

```html
<!DOCTYPE html>
<html lang="en">
<head>
<meta charset="utf-8">
<title>Harbor Compass – Book Cover</title>
<link rel="stylesheet" href="https://fonts.googleapis.com/css2?family=Cinzel:wght@400;700&family=Alegreya+Sans+SC:wght@800&display=swap">
<style>
  :root {
    --backdrop: #e9eaec;
    --cover: #ffffff;
    --navy: #1f4c9c;
    --sky: #2a8fd6;
    --wave-light: #7fd0f0;
    --wave-mid: #2fa6df;
    --wave-deep: #2a55b0;
    --stone: #6f6f72;
  }
  html, body {
    margin: 0;
    width: 1200px;
    height: 816px;
    overflow: hidden;
    background: var(--backdrop);
  }
  .book-cover {
    position: absolute;
    left: 310px;
    top: 38px;
    width: 580px;
    height: 740px;
    background: var(--cover);
    box-shadow: 0 6px 22px rgba(0, 0, 0, 0.18);
    overflow: hidden;
  }
  .wave-art {
    position: absolute;
    left: 110px;
    top: 70px;
    width: 460px;
    height: 430px;
    border-radius: 50%;
    background: radial-gradient(ellipse at 62% 60%,
      rgba(42, 85, 176, 0.55) 0%,
      rgba(47, 166, 223, 0.45) 35%,
      rgba(127, 208, 240, 0.25) 60%,
      rgba(255, 255, 255, 0) 75%);
  }
  .brand-mark {
    position: absolute;
    left: 0;
    top: 245px;
    width: 580px;
    display: flex;
    justify-content: center;
    align-items: center;
    gap: 12px;
  }
  .brand-dot {
    width: 22px;
    height: 22px;
    border-radius: 50%;
    background: var(--stone);
  }
  .brand-name {
    font-family: "Cinzel", serif;
    font-weight: 400;
    font-size: 30px;
    color: var(--navy);
  }
  .cover-title {
    position: absolute;
    left: 0;
    top: 515px;
    width: 580px;
    margin: 0;
    text-align: center;
    font-family: "Cinzel", serif;
    font-weight: 400;
    font-size: 52px;
    line-height: 64px;
    letter-spacing: 1px;
  }
  .title-first { display: block; color: var(--navy); }
  .title-second { display: block; color: var(--sky); }
  .cover-tagline {
    position: absolute;
    left: 0;
    top: 668px;
    width: 580px;
    margin: 0;
    text-align: center;
    font-family: "Alegreya Sans SC", sans-serif;
    font-weight: 800;
    font-size: 21px;
    letter-spacing: 0.5px;
    color: var(--stone);
  }
</style>
</head>
<body>
  <main class="book-cover">
    <div class="wave-art" role="img" aria-label="Sweeping blue brush-stroke wave arcing around the emblem"></div>
    <div class="brand-mark">
      <span class="brand-dot"></span>
      <span class="brand-name">Harbor Compass</span>
    </div>
    <h1 class="cover-title">
      <span class="title-first">Harbor</span>
      <span class="title-second">Compass</span>
    </h1>
    <p class="cover-tagline">Turning the Tide, One Step at a Time.</p>
  </main>
</body>
</html>
```